Magazine Design Project

Our company Villa Brunetti - www.villabrunetti.co.uk

Villa Brunetti has been established for three years and produce artisan gelato from fresh ingredients on a wholesale scale. We also cater for weddings and parties.
We supply in scoop cups, ready to scoop pans and can arrange a display freezer of 10 flavours with staff to scoop for guests.

We need a A4 full spread Magazine Advertisement (with 5mm border from the edge of the page) for a Gelato wholesaling business. It'll be advertised in a local community Indian arts magazine so needs to be eyecatching with colourful images boasting handmade artisan gelato. Most readers of this magazine will be of indian origin and self employed business owners looking for new ideas and oppurtunities and will be viewing events and productions organised by the arts company.

We pride ourselves with our inventive flavours and exceptional prices.

We would like to see designs showing colourful pans of gelato, details of what we sell and still maintaining an image of premium, quality and an authentic italian product.

Target Market(s)

Ages 20-60, Male & Female, All education levels, Self Employed who are looking to introduce this product in their food business,

Industry/Entity Type

Events

Requirements
Must have
• The design must be one A4 page and use the logo on the first page of the document we have attached - the border around the logo can be ommitted as we have done on our website www.villabrunetti.co.uk
Nice to have
• Bold colours, artisan gelato images and an authentic Italian feel
Should not have
• Should not look like it appeals to children or have images of standard ice cream cones. Avoid putting cost list on the advertisement

```html
<!DOCTYPE html>
<html lang="en">
<head>
<meta charset="utf-8">
<title>Villa Brunetti – Artisan Gelato</title>
<link rel="stylesheet" href="https://fonts.googleapis.com/css2?family=Source+Sans+3:wght@400;600;700&family=Courgette&display=swap">
<style>
  :root {
    --page-bg: #ffffff;
    --pattern-a: #e9b6d8;
    --pattern-b: #c9a9dd;
    --panel: #f6cf3f;
    --panel-edge: #ffffff;
    --pink: #e8417a;
    --blue: #1f8ad8;
    --cyan: #3cc0ec;
    --red: #e8374f;
    --red-soft: rgba(232, 55, 79, 0.82);
    --ink: #2b2b2b;
    --white: #ffffff;
  }
  * { box-sizing: border-box; margin: 0; padding: 0; }
  html, body { width: 893px; height: 1200px; overflow: hidden; background: var(--page-bg); }
  body { font-family: "Source Sans 3", sans-serif; position: relative; }

  .pattern-backdrop {
    position: absolute; left: 0; top: 0; width: 893px; height: 785px;
    background:
      radial-gradient(circle at 8% 8%, #f7a34f 0 40px, transparent 80px),
      radial-gradient(circle at 92% 6%, #f26b8a 0 40px, transparent 90px),
      radial-gradient(circle at 95% 40%, #7ad3e8 0 40px, transparent 90px),
      radial-gradient(circle at 5% 50%, #8fd4ef 0 30px, transparent 80px),
      linear-gradient(160deg, var(--pattern-a), var(--pattern-b));
  }
  .gelato-backdrop {
    position: absolute; left: 0; top: 785px; width: 893px; height: 415px;
    background: linear-gradient(120deg, #9b6a5a 0%, #e9d8c7 35%, #f3ecef 60%, #d96b7a 85%, #b6ccb0 100%);
  }

  .content-panel {
    position: absolute; left: 74px; top: 70px; width: 745px; height: 877px;
    background: var(--panel); border: 4px solid var(--panel-edge); border-radius: 26px;
    box-shadow: 0 2px 8px rgba(0,0,0,.25);
  }

  .brand-card {
    position: absolute; left: 300px; top: 23px; width: 286px; height: 190px;
    background: var(--white); border-radius: 14px;
    display: flex; flex-direction: column; align-items: center; justify-content: center; gap: 10px;
    box-shadow: 0 1px 4px rgba(0,0,0,.2);
  }
  .brand-mark { width: 46px; height: 46px; border-radius: 50%; border: 2px solid var(--ink); }
  .brand-name { font-size: 34px; font-weight: 400; color: var(--ink); letter-spacing: .5px; }
  .brand-tagline { font-size: 14px; color: var(--ink); }

  .section-title {
    position: absolute; left: 74px; width: 745px; text-align: center;
    font-family: "Courgette", cursive; font-size: 28px; line-height: 1.2;
  }
  .title-gelato { top: 226px; color: var(--pink); }
  .title-flavours { top: 474px; color: var(--cyan); }

  .about-copy {
    position: absolute; left: 100px; top: 272px; width: 693px;
    color: var(--pink); font-size: 11.2px; line-height: 1.18; font-weight: 600; text-align: center;
  }
  .about-copy p + p { margin-top: 11px; }

  .flavour-intro {
    position: absolute; left: 100px; top: 524px; width: 693px;
    color: var(--blue); font-size: 11.6px; line-height: 1.2; font-weight: 600; text-align: center;
  }

  .flavour-list {
    position: absolute; top: 558px; list-style: none;
    font-size: 11.6px; font-weight: 700; line-height: 1.1;
  }
  .flavour-list li { margin-bottom: 3.6px; }
  .flavour-list li::before { content: "• "; }
  .flavour-list small { font-size: 8px; font-weight: 700; }
  .flavour-list .note { display: block; font-size: 8px; line-height: 1.15; padding-left: 8px; }
  .col-1 { left: 86px; width: 170px; color: var(--blue); }
  .col-2 { left: 263px; width: 170px; color: var(--cyan); }
  .col-3 { left: 440px; width: 200px; color: var(--blue); }
  .col-4 { left: 646px; width: 166px; color: var(--cyan); }

  .photo {
    position: absolute; top: 791px; height: 134px; border-radius: 12px;
    box-shadow: 0 3px 8px rgba(0,0,0,.35);
  }
  .photo-sorbet { left: 93px; width: 197px; background: radial-gradient(circle at 45% 55%, #e0307a 0 40px, #f3d3da 70px, #a52a3a 100%); }
  .photo-pans { left: 350px; width: 195px; background: linear-gradient(135deg, #5a4a3c, #c9e08a 40%, #e6d2a0 60%, #6b5644); }
  .photo-counter { left: 601px; width: 196px; background: linear-gradient(135deg, #e9e2e6, #f2a7b0 45%, #c9b3a6 70%, #8a6c60); }

  .service-band {
    position: absolute; left: 86px; top: 956px; width: 731px; height: 67px;
    background: var(--red-soft); border-radius: 10px;
    color: var(--white); font-size: 11.4px; line-height: 1.18; font-weight: 600; text-align: center;
    padding: 6px 14px 0;
  }

  .contact-card {
    position: absolute; left: 283px; top: 1033px; width: 328px; height: 91px;
    background: var(--red); border-radius: 8px; color: var(--white);
    display: flex; padding: 7px 0 0 6px; font-style: normal;
  }
  .contact-address { font-size: 11.6px; line-height: 1.2; width: 189px; font-weight: 400; }
  .contact-divider { width: 1px; background: var(--white); margin: 0 10px 8px 0; }
  .contact-phones { font-size: 11.6px; line-height: 1.2; font-weight: 700; padding-top: 29px; }

  .web-band {
    position: absolute; left: 0; top: 1141px; width: 893px; height: 50px;
    background: rgba(255,255,255,.72);
    text-align: center; color: var(--pink); font-size: 32px; font-weight: 700; line-height: 50px;
  }
</style>
</head>
<body>
  <div class="pattern-backdrop" role="img" aria-label="Colourful Indian mandala pattern in orange, pink and turquoise on a lavender background"></div>
  <div class="gelato-backdrop" role="img" aria-label="Photograph of a display counter filled with pans of artisan gelato"></div>

  <div class="content-panel"></div>

  <header class="brand-card">
    <span class="brand-mark"></span>
    <span class="brand-name">Villa Brunetti</span>
    <span class="brand-tagline">The House of Italian Ice Cream</span>
  </header>

  <h2 class="section-title title-gelato">What Is Gelato?</h2>
  <div class="about-copy">
    <p>It is very common throughout the world for the word gelato to be translated into English and other languages as Ice Cream or its local equivalent. However there are significant differences between Gelato and Ice Cream.</p>
    <p>Italian gelato contains less fat than ice cream, has less incorporated air, and is served at a higher temperature. Consequently, gelato provides a greater flavour experience because there is less fat that coats the tongue, more flavour per spoonful (due to less air), and the taste buds are more alive since the temperature is not so cold as to dull their sensitivity. Not to mention fewer calories to burn!</p>
    <p>Authentic Italian gelato, on the other hand, is produced fresh practically every day in relatively small quantities, is sold directly to the public, and is available in a large number of flavours - based on fresh ingredients that make the gelato creamy and colourful. High-quality artisan gelato holds its peak flavor and smooth texture only for several days.</p>
    <p>The history of gelato dates back to frozen desserts served in ancient Rome and Egypt made from ice and snow brought down from mountaintops and preserved below ground. Later, gelato appeared during banquets at the ducal court in Florence. In fact, the Florentine cook Lorenzo Ferrata is said to have invented modern ice cream in 1565, as he presented his recipe and his innovative refrigerating techniques to the Queen of France.</p>
  </div>

  <h2 class="section-title title-flavours">Flavours of Gelato</h2>
  <p class="flavour-intro">Listed below are out popular flavours however we can produce a range of inventive flavour combinations. A member of our team are happy to discuss different flavours and answer any queries you have.</p>

  <ul class="flavour-list col-1">
    <li>Fior De Latte</li>
    <li>Vanilla</li>
    <li>Chocolate</li>
    <li>Mint Chocolate Chip</li>
    <li>Strawberry</li>
    <li>Stracciatella <small>(Chocolate Chip)</small></li>
    <li>Dulce De Leche <small>(Caramel)</small></li>
    <li>Salted Caramel</li>
    <li>Rum &amp; Raisin</li>
    <li>Cherry Ripple</li>
    <li>Cherry Yoghurt</li>
    <li>Raspberry Ripple</li>
  </ul>
  <ul class="flavour-list col-2">
    <li>Strawberry Ripple</li>
    <li>Lime Ripple</li>
    <li>Hazelnut</li>
    <li>Donatella <small>(Chocolate &amp; Hazelnut/ Hazelnut Praline)</small></li>
    <li>Pistachio <small>(Pure Sicilian)</small></li>
    <li>Tiramisu</li>
    <li>Banana</li>
    <li>Banoffee</li>
    <li>Strawberry Cheesecake</li>
    <li>Biscotti Cookie</li>
    <li>Sandwich Cookie</li>
  </ul>
  <ul class="flavour-list col-3">
    <li>Chocolate Fudge Brownie</li>
    <li>White Chocolate</li>
    <li>Coconut</li>
    <li>Coconut &amp; Chocolate <small>(Coconut Bar)</small></li>
    <li>Toffee</li>
    <li>Peanut</li>
    <li>Chocolate Chip Cookie Dough</li>
    <li>Chocolate, Peanut &amp; Caramel <small>(Nougat Bar)</small></li>
    <li>Chocolate Orange</li>
    <li>Chilli Chocolate</li>
    <li>Lemon Cream</li>
    <li>Cappuccino</li>
  </ul>
  <ul class="flavour-list col-4">
    <li>Salty Peanut</li>
    <li>Cinnamon</li>
    <li>Bubblegum <small>(Pink)</small></li>
    <li>Bubblegum <small>(Blue)</small></li>
    <li>Saffron, Apricot &amp; Almond</li>
    <li>Rose Petal</li>
    <li>Honeycomb &amp; Chocolate <small>(Honey Bar)</small></li>
    <li>Faluda <small>(with Tapioca Seeds)</small></li>
    <li>Fusion <small>(Villa's special</small><span class="note">blend of rose, saffron, cardamom, rippled with figs and vegetarian fruit jellies)</span></li>
    <li>Mango - Alphonso</li>
  </ul>

  <div class="photo photo-sorbet" role="img" aria-label="Photograph of raspberry sorbet in a glass with fresh berries and mint"></div>
  <div class="photo photo-pans" role="img" aria-label="Photograph of pans of gelato decorated with fresh fruit"></div>
  <div class="photo photo-counter" role="img" aria-label="Photograph of a gelato counter with scoops of strawberry and chocolate gelato"></div>

  <div class="service-band">
    <p>Villa Brunetti are versatile in producing flavours to meet your requirements.<br>
    From diabetic gelato to semi-freddo cakes, or just had another flavour in mind? Let us know and we'll do our very best to give you the finest Gelato available.<br>
    For any pre-orders, catering for parties or events, wholesaling, sampling or any other general enquiries and comments please contact us.</p>
  </div>

  <address class="contact-card">
    <div class="contact-address">Villa Brunetti<br>Unit 12 Meridian Trade Park<br>48 Ashdown Lane<br>East Morley<br>MR4 7QT</div>
    <div class="contact-divider"></div>
    <div class="contact-phones">Tel: 020 8000 4417<br>07700 900381<br>07700 900592</div>
  </address>

  <div class="web-band">www.villabrunetti.co.uk</div>
</body>
</html>
```